Democracy in crisis book

This book tries to sound the ALARM that we will lose our democracy unless we force Unionists to adopt the plan inside this book. I designed a mock cover (attached) but I am concerned it would not look good in the Thumbnail view that most people would see it as they're scrolling down Shopvale or Pagenook. The final title for the book is: Final Hour to Rescue the Free Republic. The current subtitle is: The Single Path to Halt the 2022 Partisan Takeover & Renew Our Homeland -- but it’s a work in progress.The subtitle is still working progress but it's really not that important and can be small.
STYLE CONSIDERATIONS:
(1) The title should be on 5 separate lines: Final; Hour; To Rescue; Free; Republic
(2) The title could be in white fat letters except for maybe one line that says “To Rescue” which could be in the blue color of the Civic Union Party-- or maybe Free Republic could be in blue. We may have to try a few variations of that.
(3) I picked the red in the mock cover to connotate an emergency,
(4) I liked big bold fat font going across the full page so that it looks like a major warning sign, though note I was unable to extend each line flush all the way to the right which I think would have been better.
(5) I liked it better flush to left instead of centered.
(6) I picked the Harwick monument + a crowd for my mock cover, but a picture of a huge crowd protesting with a picture of the United States Congress in the background would be much better. DO NOT USE HARWICK. Obviously I would need it to be an open license or something I can pay a small amount to get. If you can find that picture then the page should probably be colored in red with Congress in white.
I got the idea 4 giant title from the book “seldom a quiet so bright” and Dellowby’s “When Freedom Fades” or “Grey Herons” by Mara Vostell though I hate that font)
I love Osric Thale’s “marked since the outset” cover so if you find a picture of Congress and a protest crowd instead of painting it red you could have just a couple of jagged red stripes going across it like that cover.
I love the 3-D effect of Greta Wolven's cover for The Silverwren where it looks like a page is being ripped. That effect could be done the words Free Republic like it's being torn off the page UPDATE: MANY DESIGNERS TRIED THAT & IT DID NOT WORK AT ALL.
Note that this book will be submitted to many award competitions, so please give me an award-winning cover.
I like how the title of the book The Unchosen by Martin Fellowes has the words starting to fade. I don't like the ladder on it, but maybe 'Free Republic' could fade like that.
Unionists

```html
<!DOCTYPE html>
<html lang="en">
<head>
<meta charset="utf-8">
<title>Final Hour to Rescue the Free Republic — Cover and Spine</title>
<link rel="stylesheet" href="https://fonts.googleapis.com/css2?family=Anton&family=Source+Sans+3:wght@600;700&display=swap">
<style>
  :root {
    --stage: #d9d9d9;
    --alarm-red: #cf2229;
    --spine-red: #b81c22;
    --deep-red: #7a0f14;
    --photo-rose: #e98a7c;
    --union-blue: #2a3391;
    --white: #ffffff;
  }
  * { margin: 0; padding: 0; box-sizing: border-box; }
  html, body {
    width: 1200px;
    height: 800px;
    overflow: hidden;
    background: var(--stage);
  }
  .canvas {
    position: relative;
    width: 1200px;
    height: 800px;
  }

  /* Spine */
  .spine {
    position: absolute;
    left: 298px;
    top: 0;
    width: 70px;
    height: 800px;
    background: var(--spine-red);
    display: flex;
    flex-direction: column;
    align-items: center;
    justify-content: space-between;
    padding: 40px 0 44px;
  }
  .spine-title,
  .spine-author {
    writing-mode: vertical-rl;
    font-family: "Source Sans 3", sans-serif;
    font-weight: 700;
    white-space: nowrap;
  }
  .spine-title {
    font-size: 24px;
    letter-spacing: 0.5px;
    text-transform: uppercase;
    color: var(--white);
  }
  .spine-author {
    font-size: 24px;
    color: var(--union-blue);
  }

  /* Front cover */
  .cover {
    position: absolute;
    left: 368px;
    top: 0;
    width: 534px;
    height: 800px;
    background: var(--alarm-red);
    overflow: hidden;
  }
  .cover-photo {
    position: absolute;
    right: 0;
    top: 150px;
    width: 380px;
    height: 650px;
    background: linear-gradient(180deg,
      rgba(233,138,124,0) 0%,
      rgba(233,138,124,0.8) 16%,
      rgba(226,110,100,0.7) 36%,
      rgba(176,40,44,0.9) 55%,
      var(--deep-red) 100%);
    -webkit-mask-image: linear-gradient(90deg, transparent 0%, #000 40%);
    mask-image: linear-gradient(90deg, transparent 0%, #000 40%);
  }
  .title {
    position: absolute;
    left: 26px;
    top: 34px;
    font-family: "Anton", Impact, sans-serif;
    font-weight: 400;
    text-transform: uppercase;
    line-height: 0.9;
    z-index: 2;
  }
  .title-line { display: block; color: var(--white); }
  .title-line--final,
  .title-line--hour { font-size: 150px; }
  .title-line--rescue {
    font-size: 72px;
    color: var(--union-blue);
    margin: 4px 0 6px;
  }
  .title-line--fading {
    color: rgba(255,255,255,0.88);
    text-shadow: 0 0 10px rgba(255,255,255,0.9), 0 0 22px rgba(255,230,220,0.7);
    filter: blur(1.2px);
  }
  .title-line--free { font-size: 122px; }
  .title-line--republic { font-size: 104px; }
  .subtitle {
    position: absolute;
    right: 26px;
    top: 604px;
    width: 300px;
    font-family: "Source Sans 3", sans-serif;
    font-weight: 700;
    font-size: 18px;
    line-height: 1.2;
    color: var(--white);
    z-index: 2;
  }
  .author {
    position: absolute;
    right: 26px;
    top: 712px;
    font-family: "Source Sans 3", sans-serif;
    font-weight: 700;
    font-size: 28px;
    color: var(--white);
    z-index: 2;
  }
</style>
</head>
<body>
  <main class="canvas">
    <aside class="spine">
      <p class="spine-title">Final Hour to Rescue the Free Republic</p>
      <p class="spine-author">Corwin Hale Mc Dressel</p>
    </aside>
    <section class="cover">
      <div class="cover-photo" role="img" aria-label="Red-tinted photograph of the Capitol dome rising behind a large protest crowd"></div>
      <h1 class="title">
        <span class="title-line title-line--final">Final</span>
        <span class="title-line title-line--hour">Hour</span>
        <span class="title-line title-line--rescue">To Rescue</span>
        <span class="title-line title-line--fading title-line--free">Free</span>
        <span class="title-line title-line--fading title-line--republic">Republic</span>
      </h1>
      <p class="subtitle">The Single Path to Halt the 2022 Partisan Takeover &amp; Renew Our Homeland</p>
      <p class="author">Corwin Hale Mc Dressel</p>
    </section>
  </main>
</body>
</html>
```